Town Wordpress Design Project

Hi,
I am looking for someone to completely start from scratch on a website for a town in Texas named Brindowvale. I designed their last website about 4 years ago but am not able to give them what I would like to with my abilities. I need a wordpress website that is web 2.0 in design while still being creative. Their current website can be seen at www.brindowvale.us. They like such websites by a company named Marvenlo, you can view their town website portfolio here: http://www.marvenlo.com/index.aspx?NID=137. I would need all of the pages and info that is on their current site to be moved to the new site that I am hoping you can create for me. I want a much cleaner, nicer, and simpler navigation panel, while hiding links in drop down menus. I also want to include a calendar where they could post upcoming events and would want them to be able to add submit-able forms whenever they would need to. A search option would also be nice. I know that this is a design community, but if you could code the site as well or know someone who can, please let me know. Their Town Logo can be found attached, and the font in which you spell out their town name is totally up to you. They want their Agenda and Minutes to display like this: http://www.qwobel.com/index.aspx?NID=266. Let me know if you have any further questions...
If at all possible, I wouldn't mind the design to be designed in such a way that making it "responsive" someday would be easily possible...
Reason: More time needed for some designers...
Reason: Additional time needed...

```html
<!DOCTYPE html>
<html lang="en">
<head>
<meta charset="utf-8">
<title>Town of Brindowvale — Agendas &amp; Minutes</title>
<link rel="stylesheet" href="https://fonts.googleapis.com/css2?family=Ubuntu:wght@400;500;700&display=swap">
<style>
:root{
  --red:#c9100f;
  --red-text:#c8102e;
  --maroon-dark:#2a0a08;
  --maroon:#4f1812;
  --ink:#222;
  --muted:#444;
  --line:#e3e0de;
  --page:#fbfaf9;
  --footer:#eeeae8;
  --white:#fff;
}
*{margin:0;padding:0;box-sizing:border-box}
html,body{width:876px;height:1200px;overflow:hidden;background:var(--white)}
body{font-family:"Ubuntu",sans-serif;color:var(--ink)}
.site{width:1024px;height:1403px;transform:scale(.85547);transform-origin:0 0;position:relative;background:var(--white)}
.topline{height:4px;background:var(--maroon-dark)}
.header{height:158px;background:var(--page);position:relative}
.brand{position:absolute;left:34px;top:40px;display:flex;align-items:center;gap:12px}
.brand-mark{width:40px;height:40px;border-radius:50%;background:var(--maroon-dark)}
.brand-name{font-size:24px;font-weight:500;color:var(--maroon-dark)}
.utility{position:absolute;right:28px;top:9px;display:flex;gap:11px;font-size:12.5px}
.utility a{color:var(--red-text);text-decoration:none}
.search{position:absolute;left:734px;top:111px;width:259px;height:29px;background:var(--maroon-dark);border-radius:2px;display:flex;align-items:center;justify-content:space-between;padding:0 12px;color:#ddd;font-size:11px}
.mainnav{height:54px;background:linear-gradient(#5c1c15,#2e0c09);position:relative}
.mainnav ul{list-style:none;display:flex;height:100%;padding-left:26px}
.mainnav li{color:var(--white);font-size:13.5px;font-weight:500;padding:0 20px;display:flex;align-items:center}
.mainnav li.active{background:var(--white);color:var(--red-text);margin-top:7px;padding:0 21px;width:118px}
.dropdown{position:absolute;left:374px;top:54px;width:334px;height:96px;background:var(--page);z-index:2;display:grid;grid-template-columns:148px 160px;padding:12px 24px;row-gap:6px;font-size:11.5px;color:#333;align-content:start}
.dropdown span{line-height:18px}
.hero{height:340px;background:linear-gradient(180deg,#8aa0b0 0%,#6f7e60 18%,#5f7a3c 45%,#6e8a44 100%)}
.content{display:flex;padding:22px 0 0 17px;height:736px}
.sidebar{width:275px;border:1px solid #ececec;border-top:none;height:692px}
.side-head{background:var(--red);color:var(--white);font-size:16px;font-weight:500;height:44px;display:flex;align-items:center;padding-left:25px}
.links{list-style:none;padding:4px 0 8px}
.links li{font-size:12px;color:#333;height:28px;display:flex;align-items:center;padding-left:25px}
.news-head{margin-left:-2px;padding-left:22px;height:41px;font-size:16px}
.news{padding:16px 20px 0 20px}
.news-item{margin-bottom:17px}
.news-item h4{font-size:12.5px;font-weight:700;color:#222}
.news-item p{font-size:12px;color:#222;text-align:justify;line-height:18px}
.news-item a{font-size:12.5px;color:var(--red-text);text-decoration:none;display:block;margin-top:4px}
.main{margin-left:17px;width:688px}
.main h1{font-size:18.5px;font-weight:500;color:var(--maroon-dark);margin-top:4px}
.lead{font-size:12px;font-weight:700;line-height:18px;text-align:justify;margin-top:11px}
.main p.body{font-size:12px;line-height:18px;text-align:justify;margin-top:10px;color:#333}
.board{margin-top:24px;width:688px;border-collapse:collapse;font-size:12px;border:1px solid var(--line);border-top:none}
.board th{background:var(--maroon-dark);color:var(--white);font-weight:400;font-size:15px;height:42px;border-left:2px solid var(--white)}
.board th:first-child{border-left:none}
.board td{height:30px;border-top:1px solid var(--line);border-left:1px solid var(--line);color:#333;padding-left:16px}
.board td:first-child{padding-left:21px;border-left:none}
.board tr:nth-child(2) td{border-top:none;padding-top:10px;height:40px}
.sep{margin:0 5px;color:#333}
.footer{position:absolute;left:0;top:1292px;width:1024px;height:111px;background:var(--footer);padding:24px 22px}
.footer nav{display:flex;gap:20px;font-size:12px;font-weight:700;color:#222}
.copy{font-size:11.5px;color:#333;margin-top:16px}
</style>
</head>
<body>
<div class="site">
  <div class="topline"></div>
  <header class="header">
    <div class="brand"><span class="brand-mark"></span><span class="brand-name">Town of Brindowvale</span></div>
    <nav class="utility"><a href="#">Latest News &amp; Events</a><a href="#">City Council</a><a href="#">Police</a><a href="#">FAQ's</a><a href="#">Contact Us</a></nav>
    <div class="search"><span>enter keyword</span>
      <svg width="14" height="14" viewBox="0 0 14 14"><circle cx="6" cy="6" r="4.5" fill="none" stroke="#fff" stroke-width="2"/><line x1="9.3" y1="9.3" x2="13" y2="13" stroke="#fff" stroke-width="2.2"/></svg>
    </div>
  </header>
  <nav class="mainnav">
    <ul>
      <li>Home</li><li>My Brindowvale</li><li>Police Department</li><li class="active">City Council</li><li>Form &amp; App</li><li>Financial Tranparency</li><li>Information</li><li>Services</li>
    </ul>
    <div class="dropdown">
      <span>Election Information</span><span>Council Meeting Minutes</span>
      <span>City Secretary's Office</span><span>Town Budget</span>
      <span>Meeting Agendas</span>
    </div>
  </nav>
  <div class="hero" role="img" aria-label="Photo of horses grazing in a green pasture behind a white fence"></div>
  <div class="content">
    <aside class="sidebar">
      <div class="side-head">Information Links</div>
      <ul class="links">
        <li>Latest News &amp; Meeting Dates</li><li>Newsletters</li><li>Community &amp; Maps</li><li>Municipal Court</li><li>Public Notices</li><li>Annual Water Conservation Program</li><li>Water Customer Service</li><li>Garbage Pickup</li><li>Permits &amp; Inspections</li>
      </ul>
      <div class="side-head news-head">Latest News</div>
      <div class="news">
        <div class="news-item"><h4>20.08.2012 Information Tittle goes here</h4><p>Mauris vel lacus vitae felis vestibulum volutpat. Etiam est nunc, venenatis</p><a href="#">learn more ›</a></div>
        <div class="news-item"><h4>20.08.2012 Information Tittle goes here</h4><p>Mauris vel lacus vitae felis vestibulum volutpat. Etiam est nunc, venenatis</p><a href="#">learn more ›</a></div>
        <div class="news-item"><h4>20.08.2012 Information Tittle goes here</h4><p>Mauris vel lacus vitae felis vestibulum volutpat. Etiam est nunc, venenatis</p><a href="#">learn more ›</a></div>
      </div>
    </aside>
    <main class="main">
      <h1>Our Agendas &amp; Minutest</h1>
      <p class="lead">Lorem ipsum dolor sit amet, consectetuer adipiscing elit. Nam cursus. Morbi ut mi. Nullam enim leo, egestas id, condimentum at, laoreet mattis, massa. Sed eleifend nonummy diam.</p>
      <p class="body">Pellentesque habitant morbi tristique senectus et netus et malesuada fames ac turpis egestas. Cras id elit.3 Integer quis urna. Ut ante enim, dapibus malesuada, fringilla eu, condimentum quis, tellus. Aenean porttitor eros vel dolor. Donec convallis pede venenatis nibh. Duis quam. Nam eget lacus. Aliquam erat volutpat. Quisque dignissim congue leo.</p>
      <p class="body" style="margin-top:14px">Nulla rhoncus dictum metus. Curabitur tristique mi condimentum orci. Phasellus pellentesque aliquam enim. Proin dui lectus, cursus eu, mattis laoreet, viverra sit amet, quam</p>
      <table class="board">
        <tr><th style="width:271px">Our Board</th><th style="width:210px">Agendas</th><th>Minutes</th></tr>
        <tr><td>Town Honored</td><td>Most Recent Agenda<span class="sep">|</span>View All</td><td>Most Recent Agenda<span class="sep">|</span>View All</td></tr>
        <tr><td>Columbus Day Observed -&nbsp; Offices Closed</td><td>Most Recent Agenda<span class="sep">|</span>View All</td><td>Most Recent Agenda<span class="sep">|</span>View All</td></tr>
        <tr><td>Planning &amp; Zoning Commission</td><td>Most Recent Agenda<span class="sep">|</span>View All</td><td>Most Recent Agenda<span class="sep">|</span>View All</td></tr>
        <tr><td>Municipal Court</td><td>Most Recent Agenda<span class="sep">|</span>View All</td><td>Most Recent Agenda<span class="sep">|</span>View All</td></tr>
        <tr><td>Large Bulk Item Trash Pickup Begins</td><td>Most Recent Agenda<span class="sep">|</span>View All</td><td>Most Recent Agenda<span class="sep">|</span>View All</td></tr>
        <tr><td>Brindowvale Garden Club</td><td>Most Recent Agenda<span class="sep">|</span>View All</td><td>Most Recent Agenda<span class="sep">|</span>View All</td></tr>
        <tr><td>2010 Annual Drinking Water Quality Report</td><td>Most Recent Agenda<span class="sep">|</span>View All</td><td>Most Recent Agenda<span class="sep">|</span>View All</td></tr>
        <tr><td>Approved Budget for FY 2010-2011</td><td>Most Recent Agenda<span class="sep">|</span>View All</td><td>Most Recent Agenda<span class="sep">|</span>View All</td></tr>
        <tr><td>Town Honored</td><td>Most Recent Agenda<span class="sep">|</span>View All</td><td>Most Recent Agenda<span class="sep">|</span>View All</td></tr>
        <tr><td>Columbus Day Observed -&nbsp; Offices Closed</td><td>Most Recent Agenda<span class="sep">|</span>View All</td><td>Most Recent Agenda<span class="sep">|</span>View All</td></tr>
        <tr><td>Planning &amp; Zoning Commission</td><td>Most Recent Agenda<span class="sep">|</span>View All</td><td>Most Recent Agenda<span class="sep">|</span>View All</td></tr>
        <tr><td>Municipal Court</td><td>Most Recent Agenda<span class="sep">|</span>View All</td><td>Most Recent Agenda<span class="sep">|</span>View All</td></tr>
        <tr><td>2010 Annual Drinking Water Quality Report</td><td>Most Recent Agenda<span class="sep">|</span>View All</td><td>Most Recent Agenda<span class="sep">|</span>View All</td></tr>
        <tr><td>Approved Budget for FY 2010-2011</td><td>Most Recent Agenda<span class="sep">|</span>View All</td><td>Most Recent Agenda<span class="sep">|</span>View All</td></tr>
      </table>
    </main>
  </div>
  <footer class="footer">
    <nav><span>Home</span><span>My Brindowvale</span><span>Police Department</span><span>City Council</span><span>Form &amp; App</span><span>Financial Tranparency</span><span>Information</span><span>Services</span></nav>
    <p class="copy">Copyright © 2012 Company Name&nbsp; |&nbsp; All right reserved&nbsp;&nbsp; |&nbsp; Term &amp; Policy</p>
  </footer>
</div>
</body>
</html>
```